Lumo Quest - Main Menu - Re-Design

I want to have a refresh for this app's main menu. There are some different items on the menu depending on the language (English vs. Non-English) and version (Pro vs. Free). I have attached screenshots of the different conditions. This app is a collection of brain training games.

Need designs for light and dark mode. Need designs for both portrait and landscape mode.

Here is a link to the app in Vexo Shelf.
https://shelf.vexomarket.test/store/apps/details?id=tarnwick.lumoquest

Here is a link to the app in the Quorra App Depot.
https://apps.quorradepot.test/us/app/lumo-quest-brain-training/id573918204?ls=1&mt=8

```html
<!DOCTYPE html>
<html lang="en">
<head>
<meta charset="utf-8">
<title>Lumo Quest – Main Menu</title>
<link rel="stylesheet" href="https://fonts.googleapis.com/css2?family=Lexend:wght@400;500;600&display=swap">
<style>
  :root {
    --page-bg: #f1f5f9;
    --deco-dot: #8e929e;
    --dark-bg-inner: #3b3e5e;
    --dark-bg-outer: #252740;
    --light-bg: #f5f8fb;
    --ink-dark: #24263a;
    --ink-light: #ffffff;
    --muted-dark: #cfd1dc;
    --muted-light: #3a3c4c;
    --brand-green: #05cf9a;
    --brand-indigo: #5353fb;
    --brand-orange: #f74305;
    --brand-yellow: #f9b906;
    --nav-bg: #ffffff;
    --nav-ink: #2d3047;
    --nav-active: #05cf9a;
    --avatar-yellow: #f9b906;
    --avatar-blue: #6e9cf2;
  }
  * { box-sizing: border-box; margin: 0; padding: 0; }
  html, body { width: 1200px; height: 1200px; overflow: hidden; }
  body {
    background: var(--page-bg);
    font-family: "Lexend", "Helvetica Neue", Arial, sans-serif;
    position: relative;
  }
  .deco-dot {
    position: absolute; width: 25px; height: 25px; border-radius: 50%;
    background: var(--deco-dot); transform: translate(-50%, -50%);
  }
  .screen {
    position: absolute; top: 213px; width: 435px; height: 773px;
    overflow: hidden;
    box-shadow: 0 30px 50px rgba(120, 160, 200, 0.28);
  }
  .screen--dark {
    left: 122px;
    background: radial-gradient(circle at 50% 36%, var(--dark-bg-inner) 0%, var(--dark-bg-outer) 75%);
    color: var(--ink-light);
  }
  .screen--light {
    left: 643px;
    background: var(--light-bg);
    color: var(--ink-dark);
  }
  .avatar {
    position: absolute; left: 17px; top: 17px; width: 63px; height: 63px; border-radius: 50%;
    background: linear-gradient(180deg, var(--avatar-yellow) 0 55%, var(--avatar-blue) 55% 100%);
  }
  .app-title {
    position: absolute; left: 0; right: 0; top: 30px; text-align: center;
    font-size: 29px; font-weight: 600; letter-spacing: 0.3px;
  }
  .screen--light .app-title { color: var(--brand-green); }
  .settings-btn {
    position: absolute; left: 356px; top: 18px; width: 61px; height: 61px; border-radius: 16px;
    display: flex; align-items: center; justify-content: center;
  }
  .screen--dark .settings-btn { background: var(--brand-indigo); }
  .screen--light .settings-btn { background: var(--ink-dark); }
  .dot-grid { position: absolute; }
  .dot-grid span {
    position: absolute; width: 7px; height: 7px; border-radius: 50%;
    background: var(--deco-dot); transform: translate(-50%, -50%);
  }
  .welcome {
    position: absolute; left: 0; right: 0; top: 160px; text-align: center;
    font-size: 38px; font-weight: 500; letter-spacing: 0.5px;
  }
  .username {
    position: absolute; left: 0; right: 0; top: 227px; text-align: center;
    font-size: 19px; font-weight: 500; letter-spacing: 0.5px;
  }
  .screen--dark .username { color: var(--muted-dark); }
  .screen--light .username { color: var(--muted-light); }
  .tile {
    position: absolute; width: 174px; height: 174px; border-radius: 22px;
    color: var(--ink-light); text-align: center;
  }
  .tile--training { left: 22px; top: 304px; background: var(--brand-green); }
  .tile--games { left: 239px; top: 304px; background: var(--brand-indigo); }
  .tile--learning { left: 22px; top: 522px; background: var(--brand-orange); }
  .tile--scores { left: 239px; top: 522px; background: var(--brand-yellow); }
  .tile-art {
    position: absolute; left: 53px; top: 22px; width: 68px; height: 72px; border-radius: 18px;
    background: rgba(255, 255, 255, 0.22);
  }
  .tile--learning .tile-art, .tile--scores .tile-art { top: 42px; }
  .tile-label {
    position: absolute; left: 0; right: 0; top: 110px;
    font-size: 19px; font-weight: 400; line-height: 23px; letter-spacing: 0.6px;
  }
  .tile--learning .tile-label, .tile--scores .tile-label { top: 125px; }
  .nav-bar {
    position: absolute; left: 0; right: 0; top: 697px; height: 76px;
    background: var(--nav-bg); border-radius: 19px 19px 0 0;
  }
  .nav-item {
    position: absolute; top: 22px; width: 36px; height: 36px; margin-left: -18px;
  }
  .nav-item--center {
    top: 5px; width: 67px; height: 67px; margin-left: -33px; border-radius: 26px;
    background: var(--nav-ink); display: flex; align-items: center; justify-content: center;
  }
  .nav-indicator {
    position: absolute; left: 47px; top: 60px; width: 6px; height: 6px; border-radius: 50%;
    background: var(--nav-active);
  }
</style>
</head>
<body>

<div class="deco-dot" style="left:34px;top:47px"></div>
<div class="deco-dot" style="left:137px;top:47px"></div>
<div class="deco-dot" style="left:240px;top:47px"></div>
<div class="deco-dot" style="left:34px;top:150px"></div>
<div class="deco-dot" style="left:137px;top:150px"></div>
<div class="deco-dot" style="left:240px;top:150px"></div>
<div class="deco-dot" style="left:34px;top:253px"></div>
<div class="deco-dot" style="left:34px;top:356px"></div>
<div class="deco-dot" style="left:1167px;top:707px"></div>
<div class="deco-dot" style="left:1167px;top:810px"></div>
<div class="deco-dot" style="left:1167px;top:913px"></div>
<div class="deco-dot" style="left:1064px;top:1016px"></div>
<div class="deco-dot" style="left:1167px;top:1016px"></div>

<svg width="0" height="0" style="position:absolute">
  <defs>
    <g id="icon-gear">
      <circle cx="18" cy="18" r="11" fill="none" stroke="currentColor" stroke-width="5" stroke-dasharray="4.3 4.3"/>
      <circle cx="18" cy="18" r="9.5" fill="none" stroke="currentColor" stroke-width="2.4"/>
      <circle cx="18" cy="18" r="4" fill="none" stroke="currentColor" stroke-width="2.4"/>
    </g>
    <g id="icon-home" fill="none" stroke="currentColor" stroke-width="2.6" stroke-linejoin="round">
      <path d="M4 18 L18 5 L32 18"/>
      <path d="M8 15 V31 H14 V22 H22 V31 H28 V15"/>
    </g>
    <g id="icon-calendar" fill="none" stroke="currentColor" stroke-width="2.6">
      <rect x="5" y="6" width="26" height="26"/>
      <line x1="5" y1="12" x2="31" y2="12"/>
      <line x1="11" y1="2" x2="11" y2="8"/><line x1="25" y1="2" x2="25" y2="8"/>
      <path d="M10 17h2M15 17h2M20 17h2M25 17h1M10 22h2M15 22h2M20 22h2M25 22h1M10 27h2M15 27h2M20 27h2" stroke-width="2.4"/>
    </g>
    <g id="icon-chart" fill="none" stroke="currentColor" stroke-width="2.6">
      <rect x="4" y="12" width="7" height="20"/>
      <rect x="15" y="22" width="6" height="10"/>
      <rect x="25" y="4" width="7" height="28"/>
    </g>
    <g id="icon-brain" fill="none" stroke="#ffffff" stroke-width="2.4" stroke-linecap="round">
      <path d="M18 6 C12 4 6 8 7 13 C3 15 3 22 7 24 C7 29 12 32 18 30 C24 32 29 29 29 24 C33 22 33 15 29 13 C30 8 24 4 18 6 Z"/>
      <path d="M18 6 V30 M18 14 L13 11 M18 20 L23 17 M18 24 L13 22"/>
    </g>
  </defs>
</svg>

<!-- Dark mode -->
<section class="screen screen--dark">
  <div class="avatar" role="img" aria-label="Player avatar: friendly robot character"></div>
  <h1 class="app-title">Lumo Quest</h1>
  <div class="settings-btn"><svg width="36" height="36" viewBox="0 0 36 36" style="color:#fff"><use href="#icon-gear"/></svg></div>
  <div class="dot-grid">
    <span style="left:364px;top:114px"></span><span style="left:398px;top:114px"></span><span style="left:433px;top:114px"></span>
    <span style="left:364px;top:148px"></span><span style="left:398px;top:148px"></span><span style="left:433px;top:148px"></span>
    <span style="left:364px;top:183px"></span><span style="left:398px;top:183px"></span><span style="left:433px;top:183px"></span>
    <span style="left:364px;top:217px"></span><span style="left:398px;top:217px"></span><span style="left:433px;top:217px"></span>
    <span style="left:11px;top:481px"></span><span style="left:45px;top:481px"></span><span style="left:80px;top:481px"></span>
    <span style="left:11px;top:515px"></span><span style="left:45px;top:515px"></span><span style="left:80px;top:515px"></span>
    <span style="left:11px;top:550px"></span><span style="left:11px;top:584px"></span>
  </div>
  <p class="welcome">Welcome</p>
  <p class="username">Guest04892</p>
  <div class="tile tile--training"><div class="tile-art" role="img" aria-label="Brain with question mark illustration"></div><p class="tile-label">Training<br>Center</p></div>
  <div class="tile tile--games"><div class="tile-art" role="img" aria-label="Colourful game list illustration"></div><p class="tile-label">Game<br>List</p></div>
  <div class="tile tile--learning"><div class="tile-art" role="img" aria-label="Scroll with check mark illustration"></div><p class="tile-label">Learning</p></div>
  <div class="tile tile--scores"><div class="tile-art" role="img" aria-label="Two players at podiums illustration"></div><p class="tile-label">Scores</p></div>
  <nav class="nav-bar">
    <svg class="nav-item" style="left:50px;color:var(--nav-active)" viewBox="0 0 36 36"><use href="#icon-home"/></svg>
    <span class="nav-indicator"></span>
    <svg class="nav-item" style="left:134px;color:var(--nav-ink)" viewBox="0 0 36 36"><use href="#icon-calendar"/></svg>
    <div class="nav-item nav-item--center" style="left:217px"><svg width="36" height="36" viewBox="0 0 36 36"><use href="#icon-brain"/></svg></div>
    <svg class="nav-item" style="left:301px;color:var(--nav-ink)" viewBox="0 0 36 36"><use href="#icon-chart"/></svg>
    <svg class="nav-item" style="left:385px;color:var(--nav-ink)" viewBox="0 0 36 36"><use href="#icon-gear"/></svg>
  </nav>
</section>

<!-- Light mode -->
<section class="screen screen--light">
  <div class="avatar" role="img" aria-label="Player avatar: friendly robot character"></div>
  <h1 class="app-title">Lumo Quest</h1>
  <div class="settings-btn"><svg width="36" height="36" viewBox="0 0 36 36" style="color:#fff"><use href="#icon-gear"/></svg></div>
  <div class="dot-grid">
    <span style="left:364px;top:114px"></span><span style="left:398px;top:114px"></span><span style="left:433px;top:114px"></span>
    <span style="left:364px;top:148px"></span><span style="left:398px;top:148px"></span><span style="left:433px;top:148px"></span>
    <span style="left:364px;top:183px"></span><span style="left:398px;top:183px"></span><span style="left:433px;top:183px"></span>
    <span style="left:364px;top:217px"></span><span style="left:398px;top:217px"></span><span style="left:433px;top:217px"></span>
    <span style="left:11px;top:481px"></span><span style="left:45px;top:481px"></span><span style="left:80px;top:481px"></span>
    <span style="left:11px;top:515px"></span><span style="left:45px;top:515px"></span><span style="left:80px;top:515px"></span>
    <span style="left:11px;top:550px"></span><span style="left:11px;top:584px"></span>
  </div>
  <p class="welcome">Welcome</p>
  <p class="username">Guest04892</p>
  <div class="tile tile--training"><div class="tile-art" role="img" aria-label="Brain with question mark illustration"></div><p class="tile-label">Training<br>Center</p></div>
  <div class="tile tile--games"><div class="tile-art" role="img" aria-label="Colourful game list illustration"></div><p class="tile-label">Game<br>List</p></div>
  <div class="tile tile--learning"><div class="tile-art" role="img" aria-label="Scroll with check mark illustration"></div><p class="tile-label">Learning</p></div>
  <div class="tile tile--scores"><div class="tile-art" role="img" aria-label="Two players at podiums illustration"></div><p class="tile-label">Scores</p></div>
  <nav class="nav-bar">
    <svg class="nav-item" style="left:50px;color:var(--nav-active)" viewBox="0 0 36 36"><use href="#icon-home"/></svg>
    <span class="nav-indicator"></span>
    <svg class="nav-item" style="left:134px;color:var(--nav-ink)" viewBox="0 0 36 36"><use href="#icon-calendar"/></svg>
    <div class="nav-item nav-item--center" style="left:217px"><svg width="36" height="36" viewBox="0 0 36 36"><use href="#icon-brain"/></svg></div>
    <svg class="nav-item" style="left:301px;color:var(--nav-ink)" viewBox="0 0 36 36"><use href="#icon-chart"/></svg>
    <svg class="nav-item" style="left:385px;color:var(--nav-ink)" viewBox="0 0 36 36"><use href="#icon-gear"/></svg>
  </nav>
</section>

</body>
</html>
```